Penny auction website for high end market

need a penny auction web design , requirement as below :-

- classy and noble, as i am only selli high end products
- 25 products for the main page , 5 products per row ( please see sample picture )
- top 5 products can be highlighted as those are limited edition products
- main page , products page, members page , faq and about us page
- matching logo with the name lotvo
- clean
- responsive for desktoop
-mobile version
Updates

i missed the mobile version, i should get the mobile version aswell, for desktop it should be responsive Added Wednesday, August 16, 2017

designer may use gold or silver color too as i am selling only high end products exclusively for members only, the layout can be different than the sample, it just a guide line for the sample, other better layout would be great to see and to have.

some idea how highend feel to me https://img.kravelshop.example/scr/51200/shining-gems-flash-cms-layout_52716-original.jpg

guys, please use this design https://www.pagewrenhub.example/flash-cms-layouts/52716.html as the base , i want it high class and up market, thanks

Target Market(s)

highend products buyer

Number of Pages Required

5+ page

Font styles to use
Serif
Sans Serif
Script
Other font styles liked:
• designer match it

Colors

Designer to choose colors to be used in the design.

Requirements
Must have
• source code, logos ( use lotvo for now, will change later when confirm ) , PSD
Nice to have
• more different type of designs would be great, designers can present they ideas other than my requirement

```html
<!DOCTYPE html>
<html lang="en">
<head>
<meta charset="utf-8">
<title>LOTVO – Members</title>
<link href="https://fonts.googleapis.com/css2?family=Open+Sans:wght@400;600;700&display=swap" rel="stylesheet">
<style>
:root{
  --blue:#1583c4;
  --blue-light:#4fb2ea;
  --accent:#ef4a24;
  --text-grey:#6f6f6f;
  --topbar-bg:#f5f5f5;
  --white:#ffffff;
  --avatar-a:#d9dfe3;
  --avatar-b:#b99a84;
}
*{box-sizing:border-box;margin:0;padding:0}
html,body{width:1200px;height:1071px;overflow:hidden;background:var(--white);font-family:'Open Sans',Arial,sans-serif}
.page{position:relative;width:1200px;height:1071px}
.topbar{height:35px;background:var(--topbar-bg);display:flex;justify-content:space-between;align-items:center;padding:0 61px 0 46px;font-size:15px;color:var(--text-grey)}
.topbar-links a{color:var(--text-grey);text-decoration:none;margin-right:8px}
.topbar-links a.create{margin-left:16px}
.header{position:relative;height:111px}
.brand{position:absolute;left:43px;top:30px;font-size:42px;font-weight:700;color:var(--blue);letter-spacing:1px;line-height:1}
.search{position:absolute;left:385px;top:36px;width:428px;height:47px;border:1px solid #c8c8c8;border-radius:24px;display:flex;align-items:center;padding:0 18px;font-size:17px;font-style:italic;color:#8a8a8a;justify-content:space-between}
.join{position:absolute;left:965px;top:40px;width:172px;height:40px;background:var(--blue);color:var(--white);display:flex;align-items:center;justify-content:center;gap:10px;font-size:16px;font-weight:600}
.nav{height:58px;background:linear-gradient(180deg,var(--blue) 0%,var(--blue-light) 100%);display:flex;align-items:stretch;padding-left:43px}
.nav a{color:var(--white);text-decoration:none;font-size:16.5px;display:flex;align-items:center;padding:0 11px;margin-right:3px}
.nav a.active{background:var(--accent);padding:0 11px}
.nav a.wide{margin-right:12px}
.content{padding:0 63px 0 43px}
.title{margin-top:26px;font-size:32px;font-weight:400;color:var(--blue);line-height:1.3}
.rule{height:2px;background:var(--blue);margin:12px 0 0 -3px}
.intro{margin-top:17px;padding-left:2px;font-size:15.5px;line-height:19px;color:var(--text-grey)}
.members{position:absolute;left:-7px;top:395px;width:1190px;display:grid;grid-template-columns:repeat(5,238px);row-gap:22px}
.member{text-align:center}
.avatar{width:147px;height:147px;border-radius:50%;margin:0 auto;background:radial-gradient(circle at 50% 45%,var(--avatar-b) 0%,var(--avatar-a) 75%)}
.member-name{margin-top:6px;font-size:23px;color:var(--blue);line-height:1.2}
.member-note{font-size:17px;color:var(--text-grey);line-height:1.2}
.view-all{position:absolute;left:917px;top:889px;width:220px;height:55px;background:var(--blue);color:var(--white);font-size:21px;display:flex;align-items:center;justify-content:center}
.footer{position:absolute;left:0;top:990px;width:1200px;height:81px;background:var(--blue);color:var(--white);display:flex;justify-content:space-between;align-items:center;padding:0 63px 0 47px;font-size:19px;font-weight:600}
.footer-links span.sep{margin:0 6px}
</style>
</head>
<body>
<div class="page">
  <div class="topbar">
    <div class="topbar-links"><a href="#">Log In</a><a href="#">Sign In</a><a class="create" href="#">Create New Account</a></div>
    <div>Register and Receive 20 Free Bids !</div>
  </div>
  <header class="header">
    <div class="brand">LOTVO</div>
    <div class="search">
      <span>Search here..</span>
      <svg width="18" height="18" viewBox="0 0 18 18" aria-hidden="true"><circle cx="7.5" cy="7.5" r="5.5" fill="none" stroke="#1583c4" stroke-width="2.6"/><line x1="11.5" y1="11.5" x2="16" y2="16" stroke="#1583c4" stroke-width="2.8" stroke-linecap="round"/></svg>
    </div>
    <div class="join">
      <svg width="22" height="20" viewBox="0 0 22 20" aria-hidden="true"><path d="M11 19 L2.5 10.5 A5 5 0 0 1 11 4 A5 5 0 0 1 19.5 10.5 Z" fill="#ffffff"/></svg>
      <span>JOIN TODAY</span>
    </div>
  </header>
  <nav class="nav">
    <a class="active" href="#">HOME</a>
    <a href="#">ABOUT US</a>
    <a class="wide" href="#">ALL AUCTIONS</a>
    <a class="wide" href="#">ADVANCE SEARCH</a>
    <a class="wide" href="#" style="margin-right:18px">SHOW ALL CATEGORIES</a>
    <a href="#">CLOSED AUCTIONS</a>
  </nav>
  <main class="content">
    <h1 class="title">Members</h1>
    <div class="rule"></div>
    <p class="intro">It is a long established fact that a reader will be distracted by the readable content of a page when looking at its layout.The point of using Lorem Ipsum is that it has a more-or-less normal distribution of letters, as opposed to using 'Content here, content here', making it look like readable En-glish.</p>
  </main>
  <section class="members">
    <div class="member"><div class="avatar" role="img" aria-label="Portrait photo of member 1"></div><div class="member-name">Member 1</div><div class="member-note">loren ipsum dolar</div></div>
    <div class="member"><div class="avatar" role="img" aria-label="Portrait photo of member 2"></div><div class="member-name">Member 2</div><div class="member-note">loren ipsum dolar</div></div>
    <div class="member"><div class="avatar" role="img" aria-label="Portrait photo of member 3"></div><div class="member-name">Member 3</div><div class="member-note">loren ipsum dolar</div></div>
    <div class="member"><div class="avatar" role="img" aria-label="Portrait photo of member 4"></div><div class="member-name">Member 4</div><div class="member-note">loren ipsum dolar</div></div>
    <div class="member"><div class="avatar" role="img" aria-label="Portrait photo of member 5"></div><div class="member-name">Member 5</div><div class="member-note">loren ipsum dolar</div></div>
    <div class="member"><div class="avatar" role="img" aria-label="Portrait photo of member 6"></div><div class="member-name">Member 6</div><div class="member-note">loren ipsum dolar</div></div>
    <div class="member"><div class="avatar" role="img" aria-label="Portrait photo of member 7"></div><div class="member-name">Member 7</div><div class="member-note">loren ipsum dolar</div></div>
    <div class="member"><div class="avatar" role="img" aria-label="Portrait photo of member 8"></div><div class="member-name">Member 8</div><div class="member-note">loren ipsum dolar</div></div>
    <div class="member"><div class="avatar" role="img" aria-label="Portrait photo of member 9"></div><div class="member-name">Member 9</div><div class="member-note">loren ipsum dolar</div></div>
    <div class="member"><div class="avatar" role="img" aria-label="Portrait photo of member 10"></div><div class="member-name">Member 10</div><div class="member-note">loren ipsum dolar</div></div>
  </section>
  <a class="view-all" href="#" style="text-decoration:none">VIEW ALL</a>
  <footer class="footer">
    <div>Copyright2017.All Right Reserved</div>
    <div class="footer-links">Privacy Policy<span class="sep">|</span>Terms &amp; Conditions<span class="sep">|</span>FAQ ‘s<span class="sep">|</span>Contact Us</div>
  </footer>
</div>
</body>
</html>
```